New Years In The Smokies - New Years Eve Email Blast

Email blast encouraging guest to reserve their New Years Stay with us - showing the fireworks at The Harbor Yard in Pigeon Forge and Gatlinburg's Sky Lantern. I have attached some pictures . Must have phone number 800-316-2084

Target Market(s)

people on email list and social media platforms

Industry/Entity Type

Hotel

Colors
0356a4
85acd3
cedeed

Requirements
Must have
• 800-316-2084
• "Special Rates Available for 12/31 & 1/1"
• http://briarwoodvalleylodges.example/
Nice to have
• pictures of the area and the celebrations for New Years
Should not have
• not applicable

```html
<!DOCTYPE html>
<html lang="en">
<head>
<meta charset="utf-8">
<title>New Years In The Smokies – Email Blast</title>
<link href="https://fonts.googleapis.com/css2?family=Bebas+Neue&family=Oswald:wght@400;500&family=Dancing+Script:wght@400&family=Arimo&display=swap" rel="stylesheet">
<style>
  :root {
    --canvas: #ffffff;
    --mail-grey: #e8e8e8;
    --band-blue: #85acd3;
    --band-light: #9ccbea;
    --deep-blue: #0356a4;
    --pale-blue: #cedeed;
    --hot-pink: #ff2b8c;
    --cyan: #3fd2f6;
    --ink: #222222;
    --gold: #ffd500;
    --navy-night: #141a33;
    --link: #2a9df4;
  }
  * { margin: 0; padding: 0; box-sizing: border-box; }
  html, body { width: 1200px; height: 1200px; overflow: hidden; background: var(--canvas); }
  .sheet { position: relative; width: 1200px; height: 1200px; overflow: hidden; }

  .column { position: absolute; overflow: hidden; background: var(--mail-grey); }
  .column--full { left: 127px; top: 0; width: 347px; height: 1200px; }
  .column--zoom { left: 541px; top: 0; width: 619px; height: 1200px; background: transparent; }

  .email { position: absolute; left: 0; width: 347px; }
  .column--full .email { top: 27px; }
  .column--zoom .email { top: -48px; transform: scale(1.784); transform-origin: 0 0; }

  .hero {
    height: 244px; position: relative; text-align: center;
    background: linear-gradient(115deg, var(--hot-pink) 0%, #d46ad8 30%, var(--cyan) 60%, #6fc6f2 80%, #c05ad8 100%);
  }
  .hero__title {
    position: absolute; top: 14px; left: 0; right: 0;
    font-family: "Bebas Neue", sans-serif; font-size: 50px; line-height: 1; letter-spacing: 1px;
    color: var(--hot-pink); -webkit-text-stroke: 1px #ffd6ec;
    text-shadow: 0 0 6px rgba(255,255,255,.6);
  }
  .hero__year {
    position: absolute; top: 60px; left: 0; right: 0;
    font-family: "Bebas Neue", sans-serif; font-size: 190px; line-height: 1; letter-spacing: 2px;
    color: #a8dcf2; -webkit-text-stroke: 1px #eaf8ff;
    text-shadow: 4px 5px 0 #1d4f86, 8px 10px 14px rgba(10,30,80,.6);
  }

  .photo { position: relative; }
  .photo--celebration {
    height: 230px;
    background: radial-gradient(circle at 45% 25%, #f2a055 0%, transparent 18%),
                radial-gradient(circle at 70% 45%, #5fb8ff 0%, transparent 22%),
                linear-gradient(180deg, #5a2a4a 0%, #1a2b5a 55%, #1a1f4a 100%);
  }
  .band {
    height: 42px; background: var(--band-light); text-align: center;
    font-family: "Dancing Script", cursive; font-size: 22px; line-height: 42px; color: #2d3340;
  }
  .photo--skyline {
    height: 187px;
    background: radial-gradient(circle at 48% 5%, #f4f4e8 0%, transparent 25%),
                linear-gradient(100deg, #8a3a4a 0%, #3a6a60 50%, #1e4a48 100%);
  }
  .photo__caption {
    position: absolute; left: 89px; top: 82px;
    font-family: "Oswald", sans-serif; font-weight: 500; color: #fff; line-height: .95;
    text-shadow: 0 1px 3px rgba(0,0,0,.6);
  }
  .photo__caption span { display: block; }
  .photo__caption .sm { font-size: 25px; }
  .photo__caption .lg { font-size: 34px; }

  .rates {
    height: 202px; text-align: center; color: #fff;
    background: radial-gradient(circle at 50% 50%, #2a3258 0%, var(--navy-night) 70%);
  }
  .rates__head {
    padding-top: 62px; font-family: "Bebas Neue", sans-serif; font-size: 48px; line-height: 1;
    color: var(--gold); letter-spacing: 1px;
  }
  .rates__sub { font-family: "Bebas Neue", sans-serif; font-size: 27px; line-height: 1.1; letter-spacing: .5px; }

  .footer { height: 300px; text-align: center; color: var(--ink); }
  .footer__phone {
    padding-top: 25px; font-family: "Oswald", sans-serif; font-weight: 500;
    font-size: 40px; letter-spacing: 3px; line-height: 1.3;
  }
  .footer__rule { width: 80px; height: 2px; background: #555; margin: 10px auto 0; }
  .footer__web { margin-top: 12px; font-family: "Oswald", sans-serif; font-size: 16px; letter-spacing: 1px; }
  .footer__social { margin-top: 64px; display: flex; justify-content: center; gap: 16px; }
  .footer__social span { width: 8px; height: 8px; border-radius: 50%; background: #444; }
  .footer__legal { margin-top: 10px; font-family: "Arimo", sans-serif; font-size: 8px; line-height: 1.6; color: #333; }
  .footer__legal a { color: var(--link); text-decoration: none; }
</style>
</head>
<body>
<div class="sheet">
  <div class="column column--full">
    <div class="email">
      <header class="hero">
        <div class="hero__title">NEW YEAR EVE</div>
        <div class="hero__year">2019</div>
      </header>
      <div class="photo photo--celebration" role="img" aria-label="Fireworks and Ferris wheel over the New Year's crowd at The Harbor Yard in Pigeon Forge"></div>
      <div class="band">Stay With Us...</div>
      <div class="photo photo--skyline" role="img" aria-label="Fireworks bursting from Gatlinburg's Sky Lantern over the town">
        <div class="photo__caption"><span class="sm">NEW YEAR'S EVE</span><span class="lg">FIREWORKS</span><span class="sm">IN GATLINBURG</span></div>
      </div>
      <section class="rates">
        <div class="rates__head">SPECIAL RATES</div>
        <div class="rates__sub">AVAILABLE FOR 12/31 &amp; 1/1</div>
      </section>
      <footer class="footer">
        <div class="footer__phone">800-316-2084</div>
        <div class="footer__rule"></div>
        <div class="footer__web">WWW.BRIARWOODVALLEYLODGES.EXAMPLE</div>
        <div class="footer__social"><span></span><span></span><span></span><span></span></div>
        <div class="footer__legal">Click <a href="#">here</a> to unsubscribe. Copyright © 2017<br>All rights reserved.</div>
      </footer>
    </div>
  </div>

  <div class="column column--zoom">
    <div class="email">
      <header class="hero">
        <div class="hero__title">NEW YEAR EVE</div>
        <div class="hero__year">2019</div>
      </header>
      <div class="photo photo--celebration" role="img" aria-label="Fireworks and Ferris wheel over the New Year's crowd at The Harbor Yard in Pigeon Forge"></div>
      <div class="band">Stay With Us...</div>
      <div class="photo photo--skyline" role="img" aria-label="Fireworks bursting from Gatlinburg's Sky Lantern over the town">
        <div class="photo__caption"><span class="sm">NEW YEAR'S EVE</span><span class="lg">FIREWORKS</span><span class="sm">IN GATLINBURG</span></div>
      </div>
    </div>
  </div>
</div>
</body>
</html>
```